Armored courier complete website design
HALVORSEN
Armored courier complete website design - Security
Creative Brief
Security
www.halvorsenllc-example.com
Local armored transportation company for packages, documents, deposits, ATM's and banks. quillmark482 created original logo and personal font from zentaflow. SERVICES OFFERED BY THE HALVORSEN COMPANY (1.) Courier (a.) Cash Logistics (i.) Critical Delivery (ii.) Armored Courier Services (b.) Pharmaceutical (c.) Medical Logistics (d.) Retail & Commercial Deposit Delivery & Change Order Return Service (e.) Legal (i.) Document Delivery (ii.) Critical Courier (2.) ATM Services (a.) Installation & Removal (b.) Cash Replenishment & Deposit Removal (c.) Maintenance & Repair (i.) First Line (d.) Physical Surroundings Repair (i.) Carousel (ii.) Signage (iii.) Pilons (e.) Custom ATM Branding Solutions (f.) ATM Cleaning & Detailing (3.) Security Guard Services (a.) Corporate Security (b.) Industrial (c.) Retail (d.) Tourism & Special Events (4.) Investigative Services (a.) Corporate Investigations (b.) Workers’ Compensation Fraud Investigations (c.) Retail & Industrial (5.) Secure-Area Cleaning Services (a.) Banks & Credit Unions (b.) Industrial & Commercial (6.) Logistics (a.) Contract Logistics (b.) Critical Parts & Product Logistics (7.) Document Destruction (a.) Scheduled Programs (b.) Short term, Single Project
Would like a design similar to Belvane.com but feel free to expand from that idea. Centralized text box for images and information. Promote strength through imagery. Do not want a cookie cutter site like everyone else, i.e. Ostrel and Kellworth
left side
www.belvane.com
http://www.ostrelworld-example.com/cash-services/en
http://kellworthsecure-example.com/
Copy for each subject can be provided. Ostrelworld has a good layout of services provided, company, careers, contact us Contact us is very important -Company -Services - - - -Careers -Contact us
Halvorsen Halvorsen
The instructions provided with our latest brief updates should assist everyone in tweaking and completing the HALVORSEN design. The simplicity and elegance similar to belvane.com is all we're after. Clean lines, dark shading, stainless steel used as indicated, watermarks, chiseled edging, sharp relative images and clear/smoked borders placed as directed is what we are currently seeking. Thank you much for your efforts to date and we look forward to seeing everyone's updates per the brief updates provided below.
#96 is closest to what we are looking for. The center, scrolling buttons would be a little smaller, no border but suspended with a white, small description text at the top of each. The large, background image would have a small text description at the upper right only. This description/button could be clicked on in reference to the photo for navigation purposes. Thank you for your hard work. Much appreciated.
The bottom of the page should be entirely black with a slight fade at the top. This should cover the entire bottom of the page and be about a quarter to 1/3rd in height. The side bar should slightly bleed into this dark space. Only very small text disclosures, etc. will be placed in this black area. Thank you.
Please, no shield references at top of the navigation bar. Rectangular only. Thank you in advance.
Also, on the side, navigation bar please only put the name HALVORSEN at the top and utilize our logo at the bottom in a darker, chiseled watermark. The company name should be separated from the navigation bars via a thin line. Border the side bar identical to draft #96, i.e. transparent, and use the same darker, shaded stainless steel background behind all text as draft #96. In addition, the emphasis will be on scrolling images in the background so the width and text of navigation side bar can smaller and tighter but longer in length. Thank you for your efforts!
#96 is closest so far to what we are looking for. Left navigation bar is key. Refer all designs to Belvane.com this is the look we are going for. Spend the time on the little things, a simple design that we are looking for only works with with high quality nav bars and animation. Thank you all for your hard work!

```html
<!DOCTYPE html>
<html lang="en">
<head>
<meta charset="utf-8">
<title>Halvorsen — Armored Courier</title>
<link href="https://fonts.googleapis.com/css2?family=Open+Sans:wght@300;400;600&display=swap" rel="stylesheet">
<style>
:root{
  --ink:#f2f2f2;
  --muted:#9a9a9a;
  --steel-dark:#141618;
  --steel:#1f2225;
  --panel:rgba(18,20,22,0.92);
  --line:rgba(255,255,255,0.18);
  --footer:#050505;
  --hero-a:#0b2a40;
  --hero-b:#1d5b7e;
  --hero-c:#3c4650;
}
*{box-sizing:border-box;margin:0;padding:0}
html,body{width:1200px;height:744px;overflow:hidden;background:#000}
body{font-family:"Open Sans",Arial,sans-serif;color:var(--ink);position:relative}
.hero{position:absolute;inset:0;
  background:
   radial-gradient(circle at 830px 330px,rgba(90,180,230,0.55),transparent 260px),
   radial-gradient(circle at 1000px 200px,rgba(60,140,200,0.35),transparent 300px),
   linear-gradient(100deg,#2a2e33 0%,var(--hero-c) 30%,var(--hero-a) 60%,var(--hero-b) 85%,#4d5963 100%);}
.sidebar{position:absolute;left:72px;top:0;width:240px;height:620px}
.sidebar svg{position:absolute;inset:0}
.brand{position:absolute;left:0;top:78px;width:240px;text-align:center;font-weight:600;font-size:27px;letter-spacing:2px;color:var(--ink)}
.brand-rule{position:absolute;left:30px;right:30px;top:168px;border-top:1px solid var(--line)}
.nav{position:absolute;left:34px;top:190px;list-style:none}
.nav li{height:55px;position:relative}
.nav .label{display:block;font-size:19px;font-weight:400;letter-spacing:.5px;line-height:22px;text-transform:uppercase}
.nav .hint{display:block;font-size:13px;font-style:italic;color:var(--muted);line-height:16px}
.nav .open{position:absolute;left:234px;top:6px;width:14px;height:14px;border:1px solid var(--muted);border-radius:50%}
.mark{position:absolute;left:102px;top:524px;width:36px;height:36px;border:2px solid #bbb;border-radius:50%}
.menu{position:absolute;background:var(--panel);list-style:none;padding:4px 0}
.menu li{font-size:10.5px;text-transform:uppercase;padding:0 12px;display:flex;align-items:center;border-bottom:1px solid rgba(255,255,255,0.06)}
.services-menu{left:312px;top:298px;width:180px}
.services-menu li{height:31px}
.services-menu li.active{justify-content:space-between}
.guard-menu{left:492px;top:356px;width:192px}
.guard-menu li{height:31px}
.hero-caption{position:absolute;left:1036px;top:596px;font-size:14px}
.slider{position:absolute;left:1036px;top:626px;font-size:13px;display:flex;gap:8px;align-items:center}
.footer{position:absolute;left:0;right:0;bottom:0;height:72px;background:linear-gradient(to bottom,rgba(5,5,5,0.85),var(--footer) 30%)}
.copyright{position:absolute;left:80px;top:28px;font-size:13px;color:#cfcfcf}
.social{position:absolute;right:80px;top:22px;display:flex;gap:12px}
.social span{width:26px;height:26px;border:1.5px solid #ddd;border-radius:50%}
</style>
</head>
<body>
<div class="hero" role="img" aria-label="Businessman holding a glowing globe surrounded by digital interface icons in a server room"></div>

<aside class="sidebar">
  <svg width="240" height="620" viewBox="0 0 240 620">
    <defs>
      <linearGradient id="steel" x1="0" y1="0" x2="1" y2="1">
        <stop offset="0" stop-color="#23272b"/>
        <stop offset="1" stop-color="#0e1012"/>
      </linearGradient>
    </defs>
    <polygon points="0,0 240,0 240,520 120,620 0,520" fill="url(#steel)" fill-opacity="0.95"/>
  </svg>
  <div class="brand">HALVORSEN</div>
  <div class="brand-rule"></div>
  <ul class="nav">
    <li><span class="label">Home</span><span class="hint">back to home page</span></li>
    <li><span class="label">Company</span><span class="hint">learn about us</span></li>
    <li><span class="label">Services</span><span class="hint">what we provide</span><span class="open"></span></li>
    <li><span class="label">Careers</span><span class="hint">join our team</span></li>
    <li><span class="label">Blog</span><span class="hint">check our latest update</span></li>
    <li><span class="label">Contact</span><span class="hint">get in touch</span></li>
  </ul>
  <div class="mark"></div>
</aside>

<ul class="menu services-menu">
  <li>Courier</li>
  <li>ATM Services</li>
  <li class="active"><span>Security Guard Services</span><span>›</span></li>
  <li>Investigative Services</li>
  <li>Secure Area Cleaning Services</li>
  <li>Logistics</li>
  <li>Document Destruction</li>
</ul>
<ul class="menu guard-menu">
  <li>Corporate Security</li>
  <li>Industrial</li>
  <li>Retail</li>
  <li>Tourism &amp; Special Events</li>
</ul>

<div class="hero-caption">Learn more ➞</div>
<div class="slider"><span>❚❚</span><span>‹</span><span>›</span><span>4 / 5</span></div>

<footer class="footer">
  <p class="copyright">© 2015 All rights are reserved by Halvorsen LLC.</p>
  <div class="social"><span></span><span></span><span></span><span></span></div>
</footer>
</body>
</html>
```